Mabel's Fitness Business Cards

I would like my business cards to look expensive and sophisticated using my logo and the information below.

FRONT
Mabel’s Fitness logo

Tag line Become your happiest, healthiest and strongest self

Mabel Quint Harlow
Personal Trainer

e. mabel@mabelsfitstudio.example

t. 0781530462

w. www.mabelsfitstudio.example

```html
<!DOCTYPE html>
<html lang="en">
<head>
<meta charset="utf-8">
<title>Mabel's Fitness Business Cards</title>
<link rel="stylesheet" href="https://fonts.googleapis.com/css2?family=Oswald:wght@300;400&display=swap">
<style>
  :root {
    --stage: #5b595a;
    --paper: #ffffff;
    --ink: #231f20;
    --teal: #86b6bb;
    --taupe: #a59a98;
    --frame-dark: #9a9294;
  }
  * { margin: 0; padding: 0; box-sizing: border-box; }
  html, body { width: 1200px; height: 1200px; overflow: hidden; }
  body {
    background: var(--stage);
    font-family: "Oswald", sans-serif;
    font-weight: 300;
    position: relative;
  }
  .card {
    position: absolute;
    top: 247px;
    width: 403px;
    height: 706px;
  }
  .card--front { left: 182px; background: var(--paper); }
  .card--back { left: 615px; background: var(--ink); }
  .card__frame {
    position: absolute;
    inset: 25px;
    border: 1px solid var(--teal);
  }
  .card--back .card__frame { border-color: var(--frame-dark); }

  .brand-ring {
    position: absolute;
    left: 50%;
    transform: translateX(-50%);
    border-radius: 50%;
    border: 8px solid var(--teal);
  }
  .card--front .brand-ring { top: 190px; width: 176px; height: 176px; }
  .card--back .brand-ring { top: 248px; width: 140px; height: 140px; }

  .brand-name {
    position: absolute;
    left: 0; right: 0;
    text-align: center;
    color: var(--teal);
    font-weight: 300;
    font-size: 30px;
    letter-spacing: 0.22em;
    text-transform: uppercase;
    line-height: 1;
    padding-left: 0.22em;
  }
  .card--front .brand-name { top: 405px; }
  .card--back .brand-name { top: 418px; }

  .contact {
    position: absolute;
    left: 0; right: 0;
    top: 560px;
    text-align: center;
    color: var(--taupe);
    font-size: 22px;
    line-height: 28.5px;
  }

  .trainer {
    position: absolute;
    left: 0; right: 0;
    top: 52px;
    text-align: center;
    color: var(--taupe);
  }
  .trainer__name { font-size: 32px; font-weight: 400; line-height: 36px; }
  .trainer__role { font-size: 16px; font-weight: 400; line-height: 18px; letter-spacing: 0.01em; }

  .tagline {
    position: absolute;
    left: 0; right: 0;
    top: 550px;
    text-align: center;
    color: var(--taupe);
    font-size: 29px;
    line-height: 37.5px;
  }
</style>
</head>
<body>
  <section class="card card--front">
    <div class="card__frame"></div>
    <div class="brand-ring"></div>
    <div class="brand-name">Mabel’s Fitness</div>
    <div class="contact">
      <p>(078) 153-0462</p>
      <p>mabel@mabelsfitstudio.example</p>
      <p>www.mabelsfitstudio.example</p>
    </div>
  </section>

  <section class="card card--back">
    <div class="card__frame"></div>
    <div class="trainer">
      <p class="trainer__name">Mabel Quint Harlow</p>
      <p class="trainer__role">PERSONAL TRAINER</p>
    </div>
    <div class="brand-ring"></div>
    <div class="brand-name">Mabel’s Fitness</div>
    <div class="tagline">
      <p>Become Your Happiest,</p>
      <p>Healthiest AND</p>
      <p>Strongest Self</p>
    </div>
  </section>
</body>
</html>
```